Etiketten für Kräuterbutter Spezialitäten
Zielgruppe
Manufaktur für Kräuterbutter und Grillsaucen Spezialitäten.
Zu unseren Kunden gehören vorwiegend Privatkundschaft, welche den Genuss und vorallem die Freude am grillieren zelebrieren. Natürlich lässt sich unsere Kräuterbutter auch für spannende Pastegerichte oder andere raffinierte Gerichte verwenden.
Aufgabenstellung
- edles Designen das den Charakter der Manufaktur-Produktion rüber bringt
darf vielleicht etwas rustikal sein mit Holz oder etwas das Lust auf grillieren macht.
Vielleicht passt auch der Schiefertafelstil mit Handlettering.
- Logo Layout muss dem entsprechen wie bei allen anderen Kräuterbutter-Spezialitäten von uns.
Wir brauchen:
- Universelles Etikett für verschiedene Kräuterbutter-Spezialitäten einsetzbar
Titel: Kräuterbutter
Grösse 10cm breit x 4.5 cm hoch
Grösse 4.5 cm breit x 4.5 cm hoch
- Universelles Etikett für verschiedene Kräuterschaum-Spezialitäten. (Mit Margarine statt Butter)
Titel: Kräuterschaum
- und dementsprechen ein neutrales Logo-Etikett für einzelprodukte, welche weder mit Butter noch mit Margarine zu tun haben. (kann z.b. Eine Gewürzmischung, ein Geschenkkorb, oder eine Grillsauce sein)
Alle Lebensmittelrechtlichen relevanten Angaben sind auf dem Rücketikett.
Hier brauchen wir nur ein reines Werbeetikett für die Frontseite.

```html
<!DOCTYPE html>
<html lang="de">
<head>
<meta charset="utf-8">
<title>Kräuter Butter – Etikett</title>
<link rel="stylesheet" href="https://fonts.googleapis.com/css2?family=Kaushan+Script&family=Alfa+Slab+One&family=Roboto+Condensed:wght@700&display=swap">
<style>
  :root {
    --page-bg: #e9e9e9;
    --wood-light: #e2c898;
    --wood-mid: #cfae7a;
    --wood-dark: #b8925c;
    --ink: #2e221a;
    --grill-tone: rgba(70, 48, 32, 0.45);
    --flame-tone: rgba(46, 34, 26, 0.75);
    --accent-red: #7a2a1c;
  }
  html, body {
    margin: 0;
    width: 1200px;
    height: 1200px;
    overflow: hidden;
    background: var(--page-bg);
  }
  .canvas {
    position: relative;
    width: 1200px;
    height: 1200px;
  }
  .label {
    position: absolute;
    left: 100px;
    top: 375px;
    width: 1000px;
    height: 450px;
    overflow: hidden;
    box-shadow: 0 6px 18px rgba(0,0,0,0.15);
  }
  .label__wood {
    position: absolute;
    inset: 0;
    background: radial-gradient(ellipse at 42% 45%, var(--wood-light) 0%, var(--wood-mid) 60%, var(--wood-dark) 100%);
  }
  .label__flame {
    position: absolute;
    left: 42px;
    top: 140px;
    width: 80px;
    height: 105px;
    border-radius: 50% 50% 45% 45% / 65% 65% 35% 35%;
    background: linear-gradient(180deg, rgba(46,34,26,0.35), var(--flame-tone));
  }
  .label__grill {
    position: absolute;
    left: 835px;
    top: 70px;
    width: 140px;
    height: 360px;
    border-radius: 70px 70px 24px 24px;
    background: var(--grill-tone);
  }
  .brand-name {
    position: absolute;
    left: 0;
    right: 0;
    top: 50px;
    text-align: center;
    font-family: "Roboto Condensed", sans-serif;
    font-weight: 700;
    font-size: 52px;
    letter-spacing: 1px;
    color: var(--ink);
  }
  .title-script {
    position: absolute;
    left: 138px;
    top: 130px;
    font-family: "Kaushan Script", cursive;
    font-size: 108px;
    line-height: 1;
    color: var(--ink);
  }
  .title-block {
    position: absolute;
    left: 318px;
    top: 240px;
    font-family: "Alfa Slab One", serif;
    font-size: 104px;
    line-height: 1;
    letter-spacing: 1px;
    color: var(--ink);
  }
  .tagline {
    position: absolute;
    left: 58px;
    top: 372px;
    font-family: "Roboto Condensed", sans-serif;
    font-weight: 700;
    font-size: 30px;
    letter-spacing: 1px;
    color: var(--accent-red);
  }
</style>
</head>
<body>
<main class="canvas">
  <section class="label">
    <div class="label__wood" role="img" aria-label="Holzmaserung als Etiketthintergrund"></div>
    <div class="label__grill" role="img" aria-label="Illustration eines Kugelgrills mit Grillwender und Gabel"></div>
    <div class="label__flame" role="img" aria-label="Illustration einer Flamme"></div>
    <div class="brand-name">haldecker's</div>
    <div class="title-script">Kräuter</div>
    <div class="title-block">BUTTER</div>
    <div class="tagline">MEHR ALS NUR BEILAGE</div>
  </section>
</main>
</body>
</html>
```